Redesign digital storytelling app interface for picking topics and recording/listening to audio

We are building an app for users to tell stories to their friends and family in response to prompts. Our current interface is very basic, and we want to have it redesigned in order to make it more visually appealing and feel more like a comfortable conversation. We also need one screen created from scratch to match the existing screens.
In this app, the user picks a story topic from a list a friend has sent to them and then makes an audio recording in response to that topic. The other user receives the recording and listens to it, then responds to the story.
Attached are images of the screens we want to have redesigned.
1. Topic Selection Screen - screen showing the three prompts that the user will pick from before recording their story.
2. Story Recording Screen - screen that the user sees while recording their story.
3. Playback Screen - screen that the user sees while listening to the story.
4. Respond to Story Screen - screen that the user sees after listening to the story on the playback screen. This screen should have buttons for the user to communicate with the person who sent them the story, including: a quick record button where the user can send a voice message responding to the story, a phone call button, a text button, a chatterlane button, and a vidoru button. It should also have a button to return to the main menu.
I've also attached a graphic showing what we are currently using for a logo and color scheme. This does not need to be followed exactly.
As an added bonus, please give an example of how to manage these screens when the stories are not one-on-one, but in a group of four people.
The mood of this product should be comfortable, personal, and conversational. We want people to feel like they're chatting with an old friend. The design itself can be anything at all, so go wild!

```html
<!DOCTYPE html>
<html lang="en">
<head>
<meta charset="utf-8">
<title>Tell a Story – Recording</title>
<link href="https://fonts.googleapis.com/css2?family=Marcellus&family=Kurale&display=swap" rel="stylesheet">
<style>
  :root {
    --green: #55a22b;
    --green-dark: #3c7e1c;
    --green-text: #4f9a2a;
    --bg-light: #4a4a4a;
    --bg-dark: #202020;
    --card: #333333;
    --tag: #6a6a6a;
    --white: #ffffff;
    --grey-text: #dedede;
    --red: #d40812;
    --red-ring: #9c1218;
    --photo-sky: #8fc0e8;
    --photo-shirt: #8e8296;
  }
  html, body {
    margin: 0;
    padding: 0;
    overflow: hidden;
  }
  .screen {
    position: relative;
    width: 675px;
    height: 1200px;
    overflow: hidden;
    background: radial-gradient(ellipse 420px 620px at 340px 560px, var(--bg-light), var(--bg-dark));
    font-family: "Marcellus", serif;
    color: var(--white);
  }
  .app-header {
    position: absolute;
    left: 0; top: 0;
    width: 675px; height: 140px;
  }
  .app-header svg { display: block; }
  .app-name {
    position: absolute;
    left: 0; right: 0; top: 40px;
    text-align: center;
    font-size: 46px;
    line-height: 1;
    color: var(--white);
  }
  .screen-title {
    position: absolute;
    left: 239px; top: 136px;
    width: 195px; height: 52px;
    background: var(--tag);
    font-size: 31px;
    line-height: 52px;
    text-align: center;
    color: var(--white);
  }
  .prompt-card {
    position: absolute;
    left: 52px; top: 234px;
    width: 571px; height: 237px;
    background: var(--card);
    border-radius: 18px;
    box-shadow: inset 0 0 12px rgba(0,0,0,0.35);
  }
  .asker-photo {
    position: absolute;
    left: 0; top: 0;
    width: 237px; height: 237px;
    border-radius: 18px;
    background: linear-gradient(180deg, var(--photo-sky) 0%, #b9d3e8 55%, var(--photo-shirt) 100%);
    box-shadow: 0 6px 14px rgba(0,0,0,0.5);
  }
  .prompt-body {
    position: absolute;
    left: 248px; top: 20px;
    right: 20px;
    font-family: "Kurale", serif;
  }
  .asker-name {
    font-size: 23px;
    color: var(--green-text);
    margin: 0 0 22px;
  }
  .prompt-question {
    font-size: 25px;
    line-height: 40px;
    color: var(--grey-text);
    margin: 0;
  }
  .recording-status {
    position: absolute;
    left: 130px; width: 400px; top: 596px;
    text-align: center;
  }
  .timer {
    display: block;
    font-size: 39px;
    line-height: 48px;
  }
  .status-label {
    display: block;
    font-size: 41px;
    line-height: 48px;
  }
  .controls {
    position: absolute;
    left: 0; top: 870px;
    width: 675px; height: 200px;
  }
  .control { position: absolute; }
  .control-undo { left: 90px; top: 55px; }
  .control-record { left: 243px; top: 4px; }
  .control-play { left: 499px; top: 58px; }
  .send-button {
    position: absolute;
    left: 214px; top: 1103px;
    width: 234px; height: 47px;
    border-radius: 16px;
    background: linear-gradient(180deg, var(--green), var(--green-dark));
    color: var(--white);
    font-size: 22px;
    line-height: 47px;
    text-align: center;
    letter-spacing: 0.3px;
  }
</style>
</head>
<body>
<main class="screen">
  <header class="app-header">
    <svg width="675" height="140" viewBox="0 0 675 140" aria-hidden="true">
      <defs>
        <linearGradient id="headerFill" x1="0" y1="0" x2="0" y2="1">
          <stop offset="0" stop-color="#5aa92e"/>
          <stop offset="1" stop-color="#4a9424"/>
        </linearGradient>
        <filter id="headerShadow" x="-5%" y="-5%" width="110%" height="130%">
          <feDropShadow dx="0" dy="4" stdDeviation="5" flood-color="#000" flood-opacity="0.5"/>
        </filter>
      </defs>
      <path d="M0 0 H675 V106 Q337 160 0 106 Z" fill="url(#headerFill)" filter="url(#headerShadow)"/>
    </svg>
    <div class="app-name">LOGO</div>
  </header>

  <div class="screen-title">Tell a Story</div>

  <section class="prompt-card">
    <div class="asker-photo" role="img" aria-label="Profile photo of the friend who asked the question"></div>
    <div class="prompt-body">
      <p class="asker-name">mirelvo asks</p>
      <p class="prompt-question">Would you rather travel by plane, train, or car?</p>
    </div>
  </section>

  <div class="recording-status">
    <span class="timer">00:05</span>
    <span class="status-label">Recording</span>
  </div>

  <div class="controls">
    <svg class="control control-undo" width="92" height="100" viewBox="0 0 92 100" aria-label="Start over" role="img">
      <path d="M4 36 L40 2 L34 24 C70 26 92 48 86 74 C82 88 64 98 44 100 C66 88 74 74 70 60 C66 46 52 40 32 42 L26 62 Z" fill="#ffffff"/>
    </svg>
    <svg class="control control-record" width="190" height="190" viewBox="0 0 190 190" aria-label="Record" role="img">
      <defs>
        <radialGradient id="recordCore" cx="0.5" cy="0.45" r="0.55">
          <stop offset="0" stop-color="#e00a14"/>
          <stop offset="1" stop-color="#bd0610"/>
        </radialGradient>
      </defs>
      <circle cx="95" cy="95" r="94" fill="#8a1a1e" opacity="0.85"/>
      <circle cx="95" cy="95" r="82" fill="#c10a14"/>
      <circle cx="95" cy="95" r="64" fill="url(#recordCore)"/>
    </svg>
    <svg class="control control-play" width="84" height="86" viewBox="0 0 84 86" aria-label="Play" role="img">
      <path d="M0 0 L84 43 L0 86 Z" fill="#ffffff"/>
    </svg>
  </div>

  <div class="send-button">SEND RECORDING</div>
</main>
</body>
</html>
```